Business card design needed

I am a nutritionist and fitness instructor and I need a business card designed for my company CookRunGrow. I provide nutrition education services such as consultations, cooking demonstrations, workshops, and supermarket tours. I also provide fitness instruction and training to clients to help overhaul their lifestyle.

I would like to see designs that have a natural, organic, feel using earthy colours. I would like to have cards printed on recycled paper.

I would prefer a 2 sided card. Front side with just the business name Cook Run Grow and underneath Nutrition Health Fitness. The second side to have the contact details.

The final design should communicate health and wellness through eating organic wholefoods and being physically active.

Although I have this idea, I would be open to see other suggestions that have a similar look and feel.

Target Market(s)

people interested in being healthier, women wanting to loose weight, mothers wanting to be healthier for their families

Industry/Entity Type

Nutrition

Contact Information for Business Card

Megan Furlow
Nutritionist and Personal Trainer
M 0417382956
E cookrungrowwellness@mailbox-demo.net

Logo Text

CookRunGrow (underneath) Nutrition Health Fitness

Logo styles of interest
Wordmark Logo
Requirements
Nice to have
• I like the idea of having the letters of CookRunGrow spelt out with food such as grains, nuts, seeds, legumes, fruit etc. For example close up images of cherry tomatoes, chia seeds, kidney beans, chickpeas, blue berries, raspberries, brown rice - lots of different colours and textures. Continuing playing on the idea of the book cover Walk Sing Rest.

food is important - I am not selling supplements rather I am promoting the enjoyment of healthy wholefoods so food is important to the look and feel of the design
Should not have
• cartoon images
images associated with body building or supplements
fruit or dumb bells with tape measures around them
clichés for weight loss such as scales and tape measures
I don't want to look like other typical wellness services such as massage or spa services

```html
<!DOCTYPE html>
<html lang="en">
<head>
<meta charset="utf-8">
<title>Cook Run Grow Business Card</title>
<link rel="stylesheet" href="https://fonts.googleapis.com/css2?family=Open+Sans:wght@400;600&display=swap">
<style>
  :root {
    --bg: #e4e4e4;
    --card: #ffffff;
    --green: #8cc43f;
    --green-text: #7bb833;
    --red: #dc1a22;
    --ink: #4a4a4a;
    --grey-text: #7a7a7a;
  }
  * { margin: 0; padding: 0; box-sizing: border-box; }
  html, body {
    width: 1200px;
    height: 880px;
    overflow: hidden;
    background: var(--bg);
    font-family: "Open Sans", Arial, sans-serif;
  }
  .business-card {
    position: absolute;
    left: 100px;
    top: 160px;
    width: 1000px;
    height: 560px;
    background: linear-gradient(135deg, #ffffff 0%, #f6f6f6 60%, #ececec 100%);
    box-shadow: 0 10px 28px rgba(0,0,0,0.25);
    overflow: hidden;
  }
  .top-bands {
    position: absolute;
    top: 0;
    left: 0;
    width: 1000px;
    height: 50px;
  }
  .bottom-bands {
    position: absolute;
    bottom: 0;
    left: 0;
    width: 1000px;
    height: 12px;
  }
  .brand {
    position: absolute;
    left: 130px;
    top: 250px;
    width: 420px;
  }
  .brand-line {
    display: flex;
    align-items: center;
    gap: 16px;
  }
  .brand-mark {
    width: 22px;
    height: 22px;
    flex: none;
    background: var(--green);
  }
  .brand-name {
    font-size: 40px;
    font-weight: 400;
    color: var(--ink);
    line-height: 1;
    white-space: nowrap;
  }
  .brand-tagline {
    margin: 14px 0 0 38px;
    font-size: 13px;
    font-weight: 600;
    letter-spacing: 3px;
    text-transform: uppercase;
    color: var(--grey-text);
    line-height: 1;
    white-space: nowrap;
  }
  .person {
    position: absolute;
    right: 70px;
    top: 90px;
    text-align: right;
  }
  .person-name {
    font-size: 32px;
    color: var(--green-text);
    line-height: 1;
  }
  .person-role {
    margin-top: 8px;
    font-size: 12px;
    color: var(--red);
  }
  .contact-list {
    position: absolute;
    right: 70px;
    bottom: 78px;
    list-style: none;
    text-align: right;
  }
  .contact-item {
    display: flex;
    justify-content: flex-end;
    align-items: center;
    gap: 12px;
    font-size: 16px;
    color: var(--green-text);
    line-height: 24px;
  }
  .contact-icon {
    width: 16px;
    height: 16px;
    flex: none;
  }
</style>
</head>
<body>
  <div class="business-card">
    <svg class="top-bands" viewBox="0 0 1000 50" aria-hidden="true">
      <polygon points="0,0 262,0 228,50 0,50" fill="var(--red)"/>
      <polygon points="278,0 1000,0 1000,50 244,50" fill="var(--green)"/>
    </svg>

    <div class="brand">
      <div class="brand-line">
        <div class="brand-mark"></div>
        <div class="brand-name">Cook Run Grow</div>
      </div>
      <div class="brand-tagline">Nutrition · Health · Fitness</div>
    </div>

    <div class="person">
      <div class="person-name">Megan Furlow</div>
      <div class="person-role">Nutritionist and Personal Trainer</div>
    </div>

    <ul class="contact-list">
      <li class="contact-item">
        <span>0417382956 E</span>
        <svg class="contact-icon" viewBox="0 0 16 16" aria-hidden="true">
          <rect x="4" y="1" width="8" height="14" rx="2" fill="none" stroke="var(--red)" stroke-width="1.8"/>
          <rect x="6" y="4" width="4" height="4" fill="var(--red)"/>
        </svg>
      </li>
      <li class="contact-item">
        <span>cookrungrowwellness@mailbox-demo.net</span>
        <svg class="contact-icon" viewBox="0 0 16 16" aria-hidden="true">
          <rect x="1" y="3" width="14" height="10" fill="var(--red)"/>
          <polyline points="1,3 8,9 15,3" fill="none" stroke="#fff" stroke-width="1.4"/>
        </svg>
      </li>
      <li class="contact-item">
        <span>www.cookrungrow.net</span>
        <svg class="contact-icon" viewBox="0 0 16 16" aria-hidden="true">
          <circle cx="8" cy="8" r="6.5" fill="none" stroke="var(--red)" stroke-width="1.5"/>
          <ellipse cx="8" cy="8" rx="3" ry="6.5" fill="none" stroke="var(--red)" stroke-width="1.2"/>
          <line x1="1.5" y1="8" x2="14.5" y2="8" stroke="var(--red)" stroke-width="1.2"/>
        </svg>
      </li>
    </ul>

    <svg class="bottom-bands" viewBox="0 0 1000 12" aria-hidden="true">
      <polygon points="0,0 218,0 214,12 0,12" fill="var(--green)"/>
      <polygon points="230,0 1000,0 1000,12 226,12" fill="var(--red)"/>
    </svg>
  </div>
</body>
</html>
```